Realty Group Needs Classy, Contemporary Letterhead Design

We need a letterhead design for a new realty company located in NY, USA. We buy investment properties to rehabilitate and or keep in our rental portfolio.

```html
<!DOCTYPE html>
<html lang="en">
<head>
<meta charset="utf-8">
<title>Harborline Realty Group — Letterhead</title>
<link href="https://fonts.googleapis.com/css2?family=Quicksand:wght@500;600;700&family=Great+Vibes&display=swap" rel="stylesheet">
<style>
  :root {
    --brand-purple: #4b2a84;
    --brand-grey: #7d7d7d;
    --ink: #2b2b2b;
    --paper: #ffffff;
    --backdrop: #e3e3e3;
  }
  * { margin: 0; padding: 0; box-sizing: border-box; }
  html, body { width: 1200px; height: 1200px; overflow: hidden; background: var(--backdrop); }
  .letterhead {
    position: absolute; left: 190px; top: 20px;
    width: 820px; height: 1159px;
    background: var(--paper);
    font-family: "Quicksand", sans-serif;
    color: var(--ink);
    box-shadow: 0 4px 14px rgba(0,0,0,0.12);
  }
  .brand { position: absolute; top: 68px; left: 0; width: 100%; text-align: center; }
  .brand-name {
    font-family: "Quicksand", sans-serif; font-weight: 700;
    font-size: 50px; line-height: 1; letter-spacing: -0.5px;
    color: var(--brand-purple);
  }
  .brand-tagline {
    display: flex; align-items: center; justify-content: center; gap: 10px;
    margin-top: 6px; font-weight: 700; font-size: 18px; letter-spacing: 0.8px;
    color: var(--brand-grey);
  }
  .brand-tagline .rule { width: 62px; height: 2px; background: var(--brand-grey); }
  .recipient { position: absolute; left: 78px; top: 236px; font-size: 14.5px; line-height: 22px; font-weight: 500; }
  .salutation { position: absolute; left: 78px; top: 392px; font-size: 14.5px; font-weight: 500; }
  .body-copy {
    position: absolute; left: 78px; top: 436px; width: 664px;
    font-size: 14.5px; line-height: 22px; font-weight: 500; text-align: justify;
  }
  .signature {
    position: absolute; left: 72px; top: 836px;
    font-family: "Great Vibes", cursive; font-size: 60px; color: #111;
  }
  .footer-contact { position: absolute; left: 78px; top: 990px; font-size: 12px; color: #111; }
  .footer-address { font-weight: 700; font-size: 12.5px; line-height: 15px; margin-bottom: 6px; }
  .contact-line { display: flex; align-items: center; gap: 6px; height: 17.5px; font-weight: 500; }
  .contact-line svg { width: 10px; height: 10px; fill: none; stroke: var(--brand-purple); stroke-width: 1.4; }
  .footer-band { position: absolute; left: 0; bottom: 1px; width: 820px; height: 24px; }
</style>
</head>
<body>
<main class="letterhead">
  <header class="brand">
    <div class="brand-name">HARBORLINE</div>
    <div class="brand-tagline"><span class="rule"></span>Realty Group, LLC<span class="rule"></span></div>
  </header>

  <address class="recipient" style="font-style:normal">
    Mr. John Doe<br>President<br>Strategy Accountants<br>111 Street Name,<br>City State, 12345
  </address>

  <p class="salutation">Dear</p>

  <div class="body-copy">
    <p>Lorem ipsum dolor sit amet, consectetur adipiscing elit. Aenean ut ipsum eget massa hendrerit vestibulum vel in velit. Donec pretium neque velit.</p>
    <p>Aliquam porta lectus nec mauris ornare venenatis. Vivamus non est turpis, et cursus sem. Mauris vehicula erat in diam auctor at bibendum nisl lacinia.</p>
    <p>Morbi imperdiet neque vehicula nunc convallis gravida. Vestibulum iaculis pretium placerat. Integer consequat, est sit amet facilisis eleifend, nibh nibh varius orci, eget dapibus arcu dui non purus. Pellentesque in magna mauris. Duis enim sapien, dictum vitae condimentum a, pulvinar vel lacus. Mauris et molestie nibh. Vestibulum vitae nulla at metus elementum porta sit amet interdum elit. Nulla sollicitudin neque eu nulla volutpat congue.</p>
    <p>Etiam pellentesque, velit id dapibus fermentum, turpis sapien ornare dui, ac tincidunt ligula odio congue purus. Nunc sed ante dui, in porta lectus. Cras nec sem lorem. In hac habitasse platea dictumst. Maecenas id diam quis dui porta tristique. Sed id egestas felis. Donec ullamcorper mattis posuere. Phasellus fermentum eleifend tortor vel dapibus. Vestibulum ante ipsum.</p>
  </div>

  <div class="signature">Jonathan Doe</div>

  <footer class="footer-contact">
    <div class="footer-address">27 Hudson Ridge Road,<br>Suite 104 Kingston NY 12401</div>
    <div class="contact-line"><svg viewBox="0 0 10 10"><rect x="2.5" y="0.7" width="5" height="8.6" rx="1"/></svg>555.210.4800</div>
    <div class="contact-line"><svg viewBox="0 0 10 10"><path d="M2 1.2 L3.8 1.2 L4.4 3.3 L3.3 4.2 Q4.3 6 5.8 6.7 L6.7 5.6 L8.8 6.2 L8.8 8 Q4.5 8.6 1.4 3.6 Z"/></svg>555.210.4811</div>
    <div class="contact-line"><svg viewBox="0 0 10 10"><rect x="1" y="3.5" width="8" height="5"/><rect x="2.8" y="1" width="4.4" height="2.5"/></svg>555.210.4822</div>
    <div class="contact-line"><svg viewBox="0 0 10 10"><rect x="1" y="2" width="8" height="6"/><path d="M1 2 L5 5.5 L9 2"/></svg>jonathan@harborlinerealty.com</div>
    <div class="contact-line"><svg viewBox="0 0 10 10"><circle cx="5" cy="5" r="4"/><ellipse cx="5" cy="5" rx="1.8" ry="4"/><path d="M1 5 H9"/></svg>www.harborlinerealty.com</div>
  </footer>

  <svg class="footer-band" viewBox="0 0 820 24" preserveAspectRatio="none">
    <polygon points="0,0 278,0 266,24 0,24" fill="var(--brand-grey)"/>
    <polygon points="285,0 820,0 820,24 273,24" fill="var(--brand-purple)"/>
  </svg>
</main>
</body>
</html>
```